Bright Tooth Dentistry Business Card

We need business cards for our dental office.
We are looking for a clean, elegant design

We provide dental services to children.
Our card needs to be appealing to referring dentists, parents and our team

Target Market(s)

referring dentists, parents and our team

Industry/Entity Type

Dental Clinic

Contact Information for Business Card

4816 Juniper Lane, Suite 210
Fairview Hills, PA 15237

412-837-2961 Voice
412-837-2962 fax
info@brighttoothdentalpa.com email
www.brighttoothdentalpa.com web

Font styles to use
Sans Serif

Requirements
Must have
• White background - clean, crisp, elegant, simple
• rounded corners
• different color palate - once we come up with design, we will replace the blue with orange, green,
Nice to have
• Follow our logo typeface and colors
• then we can replace color

```html
<!DOCTYPE html>
<html lang="en">
<head>
<meta charset="utf-8">
<title>Bright Tooth Dentistry Business Card</title>
<link rel="stylesheet" href="https://fonts.googleapis.com/css2?family=Outfit:wght@400;500&display=swap">
<style>
  :root {
    --backdrop: #e8e4dd;
    --brand-green: #4cae3f;
    --brand-orange: #ee8e35;
    --card-white: #f1f1ef;
    --ink: #1d1d1d;
    --shadow: 0 6px 16px rgba(0,0,0,0.28);
  }
  * { margin: 0; padding: 0; box-sizing: border-box; }
  html, body {
    width: 900px; height: 1200px; overflow: hidden;
    background: var(--backdrop);
    font-family: "Outfit", sans-serif;
  }
  .canvas { position: relative; width: 900px; height: 1200px; }

  .card {
    position: absolute;
    border-radius: 18px;
    overflow: hidden;
    box-shadow: var(--shadow);
  }
  .card-front {
    left: 86px; top: 137px; width: 737px; height: 433px;
    background: var(--brand-green);
  }
  .logo-oval { position: absolute; left: 0; top: 0; }
  .brand-name {
    position: absolute; left: 0; right: 0; top: 228px;
    text-align: center;
    font-size: 44px; font-weight: 500; line-height: 1;
    color: var(--brand-orange);
    letter-spacing: 0.2px;
  }

  .card-back {
    left: 81px; top: 632px; width: 742px; height: 431px;
    background: var(--card-white);
  }
  .brand-panel {
    position: absolute; left: 0; top: 0; width: 295px; height: 100%;
    background: var(--brand-orange);
    display: flex; align-items: center; justify-content: center;
  }
  .brand-panel-name {
    color: #ffffff;
    font-size: 34px; font-weight: 500; line-height: 1.15;
    text-align: center;
  }
  .contact-list { list-style: none; }
  .contact-item {
    position: absolute; left: 324px;
    display: flex; align-items: center; gap: 15px;
    font-size: 20px; font-weight: 400; color: var(--ink);
    letter-spacing: 1.2px; line-height: 1.55;
  }
  .contact-icon { width: 39px; height: 39px; flex: none; }
</style>
</head>
<body>
<main class="canvas">

  <section class="card card-front" aria-label="Card front">
    <svg class="logo-oval" width="737" height="433" viewBox="0 0 737 433" aria-hidden="true">
      <ellipse cx="369" cy="215" rx="260" ry="164" fill="var(--card-white)"/>
      <ellipse cx="369" cy="215" rx="250" ry="154" fill="none" stroke="var(--brand-green)" stroke-width="3"/>
    </svg>
    <div class="brand-name">Bright Tooth Dentistry</div>
  </section>

  <section class="card card-back" aria-label="Card back">
    <div class="brand-panel">
      <div class="brand-panel-name">Bright Tooth<br>Dentistry</div>
    </div>

    <ul class="contact-list">
      <li class="contact-item" style="top:70px">
        <svg class="contact-icon" viewBox="0 0 38 38" aria-hidden="true">
          <circle cx="19" cy="19" r="19" fill="var(--brand-green)"/>
          <path d="M13 10c1-1 2.5-1 3 0l2 4c.4.8 0 1.6-.6 2l-1.2 1c.8 2 2.6 3.8 4.6 4.6l1-1.2c.5-.6 1.3-1 2-.6l4 2c1 .5 1 2 0 3l-1.6 1.6c-1 1-3 1-5-.2-4-2.2-7-5.2-9.2-9.2-1.2-2-1.2-4-.2-5z" fill="#fff"/>
        </svg>
        <span>412-837-2961</span>
      </li>
      <li class="contact-item" style="top:119px">
        <svg class="contact-icon" viewBox="0 0 38 38" aria-hidden="true">
          <circle cx="19" cy="19" r="19" fill="var(--brand-green)"/>
          <rect x="13" y="9" width="12" height="7" fill="#fff"/>
          <rect x="9" y="15" width="20" height="10" rx="2" fill="#fff"/>
          <rect x="13" y="21" width="12" height="8" fill="#fff" stroke="var(--brand-green)" stroke-width="1.5"/>
        </svg>
        <span>412-837-2962</span>
      </li>
      <li class="contact-item" style="top:182px">
        <svg class="contact-icon" viewBox="0 0 38 38" aria-hidden="true">
          <circle cx="19" cy="19" r="19" fill="var(--brand-green)"/>
          <path d="M19 8a7 7 0 0 1 7 7c0 5-7 14-7 14s-7-9-7-14a7 7 0 0 1 7-7z" fill="#fff"/>
          <circle cx="19" cy="15" r="2.8" fill="var(--brand-green)"/>
        </svg>
        <span>4816 Juniper Lane, Suite 210<br>Fairview Hills, PA 15237</span>
      </li>
      <li class="contact-item" style="top:277px">
        <svg class="contact-icon" viewBox="0 0 38 38" aria-hidden="true">
          <circle cx="19" cy="19" r="19" fill="var(--brand-green)"/>
          <rect x="9" y="12" width="20" height="14" rx="1.5" fill="#fff"/>
          <path d="M9.5 13l9.5 7 9.5-7" fill="none" stroke="var(--brand-green)" stroke-width="1.6"/>
        </svg>
        <span>info@brighttoothdentalpa.com</span>
      </li>
      <li class="contact-item" style="top:326px">
        <svg class="contact-icon" viewBox="0 0 38 38" aria-hidden="true">
          <circle cx="19" cy="19" r="19" fill="var(--brand-green)"/>
          <g fill="none" stroke="#fff" stroke-width="1.6">
            <circle cx="19" cy="19" r="10"/>
            <ellipse cx="19" cy="19" rx="4.5" ry="10"/>
            <path d="M9 19h20M11 14h16M11 24h16"/>
          </g>
        </svg>
        <span>brighttoothdentalpa.com</span>
      </li>
    </ul>
  </section>

</main>
</body>
</html>
```